Brisk Canopy Builders needs a product brochure

We need a new flyer for our Porch Nook Lounge. Here is some of the copy your will need.
"Turn your back yard into the ultimate entertianment venue with the stunning Porch Nook Lounge!"
"Entertain family & friends in your very own back yard!"
"Available with or without solar and comes in a variety of colors"
"The Porch Nook Lounge measures 5' deep by 10' wide and is 9'-6" at it's highest point"
"Constructed with treated 4x4's, primed then painted with Garrick Pellman best exterior paint for years of care free enjoyment. Also, Farley Dunmore Steadfast shingles are dimensional, have a 25 year warranty and are rated for 150 mph winds!"
"TV Mount included. Shelves and TV are sold separately"
There also needs to be a box where we can add the price into later. The price can change from time to time due to material cost fluctuation.

```html
<!DOCTYPE html>
<html lang="en">
<head>
<meta charset="utf-8">
<title>Porch Nook Lounge Flyer</title>
<link href="https://fonts.googleapis.com/css2?family=Barlow:wght@400;500;600;700;800;900&display=swap" rel="stylesheet">
<style>
  :root{
    --green:#2a7a34;
    --green-dark:#1f6a2b;
    --green-light:#3c9a46;
    --orange:#f5a81c;
    --white:#ffffff;
    --ink:#222222;
    --backdrop:#e4e4e6;
  }
  *{margin:0;padding:0;box-sizing:border-box}
  html,body{width:1200px;height:892px;overflow:hidden;background:var(--backdrop);font-family:"Barlow",sans-serif}
  .flyer{position:absolute;left:300px;top:22px;width:600px;height:848px;background:var(--white);overflow:hidden;box-shadow:0 6px 24px rgba(0,0,0,.18)}
  .flyer-shapes{position:absolute;inset:0}
  .brand{position:absolute;left:26px;top:34px;display:flex;align-items:center;gap:7px}
  .brand-mark{width:12px;height:12px;border-radius:50%;background:var(--green)}
  .brand-name{font-weight:800;font-size:15px;color:var(--green);letter-spacing:.4px;line-height:1.05;text-transform:uppercase}
  .band-title{position:absolute;left:32px;top:384px;font-weight:800;font-size:26px;line-height:.98;color:var(--white);text-transform:uppercase}
  .band-title .accent{color:var(--orange);font-size:26px;margin-left:6px}
  .venue-badge{position:absolute;left:320px;top:292px;width:300px;height:196px;display:flex;flex-direction:column;align-items:center;justify-content:center;text-align:center;text-transform:uppercase}
  .venue-lead{color:var(--white);font-weight:700;font-size:14px;line-height:1.1}
  .venue-head{color:var(--orange);font-weight:900;font-size:27px;line-height:1;margin-top:6px}
  .thumb{position:absolute;border:5px solid var(--green);border-radius:20px}
  .thumb-drink{left:34px;top:492px;width:160px;height:92px;background:linear-gradient(135deg,#7c9a5c,#c7a27a 55%,#3f4a45)}
  .thumb-rack{left:204px;top:492px;width:160px;height:92px;background:linear-gradient(135deg,#b0703a,#6c4a2a 50%,#3a3d40)}
  .tagline{position:absolute;left:384px;top:500px;width:210px;text-align:center;font-size:16px;font-weight:500;color:var(--ink);line-height:1.15}
  .tagline strong{display:block;color:var(--green);font-weight:800;font-size:17px}
  .features{position:absolute;left:30px;top:594px;width:370px;background:var(--green);border-radius:22px;padding:14px 18px 12px 20px;list-style:none}
  .features li{position:relative;color:var(--white);font-size:11.5px;line-height:1.25;padding-left:15px;margin-bottom:4px}
  .features li:last-child{margin-bottom:0}
  .features li::before{content:"";position:absolute;left:0;top:4px;width:7px;height:7px;border-radius:50%;background:var(--white)}
  .price-box{position:absolute;left:414px;top:590px;width:164px;height:150px;border-radius:22px;background:linear-gradient(150deg,var(--green-dark),var(--green-light) 60%,var(--green));padding:22px 14px;text-align:center}
  .price-label{color:var(--white);font-size:21px;font-weight:500;line-height:1.05;text-transform:uppercase}
  .contact{position:absolute;left:0;bottom:0;width:100%;height:58px;background:var(--orange);display:flex;align-items:center;justify-content:space-around;padding:0 20px}
  .contact-item{display:flex;align-items:center;gap:7px;color:var(--white);font-size:13px;font-weight:600}
  .contact-item svg{width:16px;height:16px}
</style>
</head>
<body>
<div class="flyer">
  <svg class="flyer-shapes" viewBox="0 0 600 848" aria-hidden="true">
    <defs>
      <linearGradient id="heroTone" x1="0" y1="0" x2="1" y2="1">
        <stop offset="0" stop-color="#6f9a4a"/>
        <stop offset=".35" stop-color="#4a4e52"/>
        <stop offset=".65" stop-color="#b0753c"/>
        <stop offset="1" stop-color="#9a9a98"/>
      </linearGradient>
    </defs>
    <path d="M240 0 H600 V275 Q420 362 0 392 V328 Q120 160 240 0 Z" fill="var(--orange)"/>
    <path d="M600 252 Q560 300 520 318 L600 300 Z" fill="var(--green)"/>
    <path d="M0 372 Q240 352 420 336 V432 Q230 446 0 478 Z" fill="var(--green)"/>
    <path d="M598 460 Q588 500 572 520" stroke="var(--orange)" stroke-width="4" fill="none"/>
    <path d="M400 775 L600 755 V790 L400 800 Z" fill="var(--orange)"/>
    <ellipse cx="470" cy="390" rx="150" ry="98" fill="var(--green)" stroke="var(--white)" stroke-width="4"/>
  </svg>
  <svg class="flyer-shapes" viewBox="0 0 600 848" role="img" aria-label="Photo of the Porch Nook Lounge outdoor bar with solar panel roof, mounted TV, shelves and bar stools on a patio">
    <path d="M266 0 H600 V250 Q420 340 40 358 Q150 160 266 0 Z" fill="url(#heroTone)"/>
  </svg>

  <div class="brand">
    <span class="brand-mark"></span>
    <span class="brand-name">Brisk Canopy<br>Builders</span>
  </div>

  <h2 class="band-title">Turn<br>Your<span class="accent">Back Yard Into</span></h2>

  <div class="venue-badge">
    <p class="venue-lead">The Ultimate<br>Entertainment Venue<br>With</p>
    <h1 class="venue-head">The Stunning<br>Porch Nook<br>Lounge!</h1>
  </div>

  <div class="thumb thumb-drink" role="img" aria-label="Photo of a hand holding a drink beside a football on the bar counter"></div>
  <div class="thumb thumb-rack" role="img" aria-label="Photo of a wooden wine shelf with bottles and hanging glasses"></div>

  <p class="tagline">Entertain family &amp; friends<br>in your<strong>very own back yard!</strong></p>

  <ul class="features">
    <li>Available with or without solar and comes in a variety of colors</li>
    <li>The Porch Nook Lounge measures 5' deep by 10' wide and is 9'-6" at it's highest point</li>
    <li>TV Mount included. Shelves and TV are sold separately</li>
    <li>Constructed with treated 4x4's, primed then painted with Garrick Pellman best exterior paint for years of care free enjoyment. Also, Farley Dunmore Steadfast shingles are dimensional, have a 25 year warranty and are rated for 150 mph winds!</li>
  </ul>

  <div class="price-box">
    <p class="price-label">Starting<br>at just</p>
  </div>

  <footer class="contact">
    <span class="contact-item">
      <svg viewBox="0 0 16 16"><circle cx="8" cy="8" r="8" fill="#fff"/><rect x="4" y="5" width="8" height="6" fill="none" stroke="#f5a81c" stroke-width="1.2"/><path d="M4 5 L8 8.5 L12 5" fill="none" stroke="#f5a81c" stroke-width="1.2"/></svg>
      info@briskcanopybuilders.com
    </span>
    <span class="contact-item">
      <svg viewBox="0 0 16 16"><circle cx="8" cy="8" r="8" fill="#fff"/><circle cx="8" cy="8" r="4.5" fill="none" stroke="#f5a81c" stroke-width="1.2"/><path d="M3.5 8 H12.5 M8 3.5 V12.5" stroke="#f5a81c" stroke-width="1"/></svg>
      www.briskcanopybuilders.com
    </span>
    <span class="contact-item">
      <svg viewBox="0 0 16 16"><circle cx="8" cy="8" r="8" fill="#fff"/><path d="M5 4.5 L6.6 4.3 L7.3 6.3 L6.4 7 Q7.2 8.8 9 9.6 L9.7 8.7 L11.7 9.4 L11.5 11 Q8.6 11.4 6.6 9.4 Q4.6 7.4 5 4.5 Z" fill="#f5a81c"/></svg>
      555-014-2290
    </span>
  </footer>
</div>
</body>
</html>
```